Large and Small Oval Label

This will be for a medium 2 1/2h x 3 1/2w oval, 8 oz.. and a small 1 1/2h x 2 1/2w oval, 4 oz.. Same Design and product information. Different sizes. My "old" label is attached. My logo, also attached, needs to be added. Sample information, attached with notes in Powerpoint.. Font type is the same as the "old" label. I do not want lines going across the oval like the "old" label. Natural color label.

Please note: The top edge on the "old" label that list the "cautions". I need this shift down to the bottom edge of the label instead of at the top.

Thanks!! m

Product

```html
<!DOCTYPE html>
<html lang="en">
<head>
<meta charset="utf-8">
<title>Rose Meadow – Oval Label 8 oz</title>
<link rel="stylesheet" href="https://fonts.googleapis.com/css2?family=Dancing+Script:wght@400;500&family=Roboto+Condensed:wght@400&display=swap">
<style>
  :root {
    --paper: #ffffff;
    --label-rim: #e4d7b0;
    --label-face: #f0ead0;
    --ink-dark: #86694a;
    --ink-soft: #b69d76;
    --ornament: #8a6b4b;
  }
  html, body {
    margin: 0;
    padding: 0;
    width: 1200px;
    height: 901px;
    overflow: hidden;
    background: var(--paper);
  }
  .label {
    display: block;
    width: 1200px;
    height: 901px;
  }
  .label-rim { fill: var(--label-rim); }
  .label-face { fill: var(--label-face); }
  .label-frame { fill: none; stroke: var(--ink-dark); stroke-width: 3.2; }
  .divider { stroke: var(--ink-soft); stroke-width: 2; stroke-dasharray: 2 3.5; }
  .ornament { fill: var(--ornament); }
  .brand-name {
    font-family: "Dancing Script", cursive;
    font-size: 70px;
    fill: var(--ink-dark);
  }
  .product-line {
    font-family: "Dancing Script", cursive;
    font-size: 42px;
    fill: var(--ink-soft);
  }
  .slogan {
    font-family: "Dancing Script", cursive;
    font-weight: 500;
    font-size: 46px;
    fill: var(--ink-dark);
  }
  .web-address {
    font-family: "Dancing Script", cursive;
    font-size: 36px;
    fill: var(--ink-soft);
  }
  .net-weight {
    font-family: "Roboto Condensed", "Arial Narrow", sans-serif;
    font-size: 30px;
    fill: var(--ink-dark);
  }
  .caution {
    font-family: "Roboto Condensed", "Arial Narrow", sans-serif;
    font-size: 18px;
    fill: var(--ink-soft);
  }
</style>
</head>
<body>
<svg class="label" viewBox="0 0 1200 901" xmlns="http://www.w3.org/2000/svg">
  <defs>
    <path id="caution-arc" d="M 151 446 A 445 304 0 0 0 1041 446"/>
  </defs>

  <ellipse class="label-rim" cx="594" cy="452" rx="520" ry="368"/>
  <ellipse class="label-face" cx="596" cy="448" rx="462" ry="313"/>
  <ellipse class="label-frame" cx="596" cy="446" rx="404" ry="268"/>

  <rect class="ornament" x="94" y="346" width="124" height="204" rx="56" role="img" aria-label="Left floral flourish ornament"/>
  <rect class="ornament" x="976" y="346" width="124" height="204" rx="56" role="img" aria-label="Right floral flourish ornament"/>

  <text class="brand-name" x="598" y="328" text-anchor="middle">Rose Meadow</text>

  <line class="divider" x1="264" y1="370" x2="930" y2="370"/>
  <text class="product-line" x="598" y="428" text-anchor="middle">Natural&#160; Bath &amp; Body&#160; Skin Therapy</text>
  <line class="divider" x1="264" y1="456" x2="930" y2="456"/>

  <text class="slogan" x="594" y="520" text-anchor="middle">"Simply Authentic"</text>
  <text class="web-address" x="598" y="608" text-anchor="middle">www.rosemeadowstore.com</text>
  <text class="net-weight" x="598" y="688" text-anchor="middle">Net wt : 8 oz</text>

  <text class="caution">
    <textPath href="#caution-arc" startOffset="50%" text-anchor="middle">Caution: For external use only. Avoid contact with eyes. May stain fabrics. Store at room temperature.</textPath>
  </text>
</svg>
</body>
</html>
```